bluegate mental health stationary

Please help turn this logo into a total image for my business.
Stationary need to be able to be individualized for each mental health practitioners

Some generic info about services
Clinical Psychology - Consultant Psychiatry - Locum Services - Medico-legal - Architectural Adviser Clinical and Medical Facilities

Target Market(s)

Letter head for doctors, courts, patients.

Industry/Entity Type

Mental Health

Requirements
Must have
• area where practitioners details can be listed and logo on page
Nice to have
• embossed section

```html
<!DOCTYPE html>
<html lang="en">
<head>
<meta charset="utf-8">
<title>Bluegate Mental Health – Letterhead</title>
<link rel="stylesheet" href="https://fonts.googleapis.com/css2?family=Arimo:wght@400;700&family=Pinyon+Script&display=swap">
<style>
  :root {
    --brand-blue: #1a8fc0;
    --brand-navy: #1f4a6b;
    --text-dark: #222222;
    --text-grey: #444444;
    --rule-blue: #2a9bd0;
    --panel-grey: #f2f2f2;
    --band-start: #0b92b8;
    --band-end: #153d5c;
    --paper: #ffffff;
  }
  * { box-sizing: border-box; margin: 0; padding: 0; }
  html, body { width: 928px; height: 1200px; overflow: hidden; background: var(--paper); }
  .letterhead {
    position: relative; width: 928px; height: 1200px; overflow: hidden;
    background: var(--paper); font-family: "Arimo", Arial, sans-serif; color: var(--text-dark);
  }
  .practitioner { position: absolute; left: 42px; top: 34px; }
  .practitioner-name { font-size: 17px; color: var(--brand-blue); line-height: 22px; }
  .practitioner-meta { font-size: 14.5px; color: var(--text-grey); line-height: 20px; }

  .brand { position: absolute; left: 395px; top: 44px; display: flex; align-items: center; gap: 12px; }
  .brand-square { width: 62px; height: 62px; background: var(--brand-navy); }
  .brand-name { font-size: 17px; font-weight: 700; color: var(--brand-navy); line-height: 24px; letter-spacing: 0.3px; text-transform: uppercase; white-space: nowrap; }

  .contact-rule { position: absolute; left: 666px; top: 42px; width: 1px; height: 52px; background: var(--rule-blue); }
  .contact { position: absolute; left: 655px; top: 38px; font-size: 10px; color: var(--text-grey); line-height: 14px; font-style: normal; }
  .contact-line { display: flex; align-items: center; gap: 4px; padding-left: 12px; }
  .contact-line svg { width: 10px; height: 10px; fill: var(--brand-blue); flex: none; }
  .contact-reg { color: var(--text-grey); }
  .contact-reg span { color: var(--brand-blue); }
  .contact-web { color: var(--brand-blue); line-height: 11px; }

  .side-panel { position: absolute; left: 668px; top: 768px; width: 260px; height: 360px; background: var(--panel-grey); }

  .salutation { position: absolute; left: 62px; top: 203px; font-size: 16.5px; }
  .letter-body { position: absolute; left: 132px; top: 240px; width: 706px; }
  .letter-body p { font-size: 16.6px; line-height: 20.6px; margin-bottom: 20.6px; }

  .signature { position: absolute; left: 54px; top: 880px; font-family: "Pinyon Script", cursive; font-size: 50px; color: var(--text-dark); }

  .services-band {
    position: absolute; left: 0; top: 1128px; width: 928px; height: 72px;
    background: linear-gradient(90deg, var(--band-start), var(--band-end));
    color: #ffffff; font-size: 16.5px; text-align: center; padding-top: 7px; line-height: 23px;
  }
  .services-row { display: flex; justify-content: center; align-items: center; gap: 22px; }
  .services-row .dot { width: 8px; height: 8px; border-radius: 50%; background: #ffffff; }
</style>
</head>
<body>
<main class="letterhead">
  <header>
    <div class="practitioner">
      <div class="practitioner-name">Doctor’s Name</div>
      <div class="practitioner-meta">Qualifications</div>
      <div class="practitioner-meta">Description</div>
    </div>

    <div class="brand">
      <div class="brand-square"></div>
      <div class="brand-name">Bluegate<br>Mental Health</div>
    </div>

    <div class="contact-rule"></div>
    <address class="contact">
      <div class="contact-line"><svg viewBox="0 0 12 12"><path d="M6 0a4 4 0 0 0-4 4c0 3 4 8 4 8s4-5 4-8a4 4 0 0 0-4-4zm0 5.5A1.5 1.5 0 1 1 6 2.5a1.5 1.5 0 0 1 0 3z"/></svg>24 Harlow Court, WESTMERE 6031</div>
      <div class="contact-line"><svg viewBox="0 0 12 12"><path d="M2.5 0.5l2 2-1 1.5c.8 1.7 2.3 3.2 4 4l1.5-1 2 2-1.5 2C5 10.5 1.5 7 0.5 2z"/></svg>(08) 9312 4870 or 0412 508 736</div>
      <div class="contact-line"><svg viewBox="0 0 12 12"><path d="M3.5 0h5a1 1 0 0 1 1 1v10a1 1 0 0 1-1 1h-5a1 1 0 0 1-1-1V1a1 1 0 0 1 1-1zm.5 1.5v7.5h4V1.5z"/></svg>+000 000 0000</div>
      <div class="contact-line"><svg viewBox="0 0 12 12"><path d="M0 2.5h12v7H0zm1 1v.3l5 3 5-3v-.3z"/></svg>name@bgmh.net.au</div>
      <div class="contact-reg"><span>ABN:</span>41 208 665 917 &nbsp;&nbsp;&nbsp;<span>ACN:</span>148207392</div>
      <div class="contact-web">www.bluegatementalhealth.com</div>
    </address>
  </header>

  <div class="side-panel"></div>

  <section class="letter">
    <p class="salutation">Dear Sir / Madam,</p>
    <div class="letter-body">
      <p>Lorem ipsum dolor sit amet, consectetur adipisicing elit, sed do eiusmod tempor labore et olore magna aliqua. Ut enim ad minim veniam, quis nostrud exercitation ullamco laboris nisi ut aliquip ex ea commodo consequa.Lorem ipsum dolor sit amet, nsectetur adipisicing elit, sed do eiusmod tempor incididunt ut labore et dolore magna aliqua. Ut enim ad minim veniam, quis.</p>
      <p>Lorem ipsum dolor sit amet, consectetur adipisicing elit, sed do eiusmod tempor labore et dolore magna aliqua. Ut enim ad minim veniam, quis nostrud exercitation ullamco laboris nisi ut aliquip ex ea commodo consequa.Lorem ipsum dolor sit amet, nsectetur adipisicing elit, sed do eiusmod tempor incididunt ut labore et dolore magna aliqua. Ut enim ad minim veniam, quis.</p>
      <p>Lorem ipsum dolor sit amet, consectetur adipisicing elit, sed do eiusmod tempor labore et dolore magna aliqua. Ut enim ad minim veniam, quis nostrud exercitation ullamco laboris nisi ut aliquip ex ea commodo consequa.Lorem ipsum dolor sit amet, nsectetur adipisicing elit, sed do eiusmod tempor incididunt ut labore et dolore magna aliqua. Ut enim ad minim veniam, quis.</p>
      <p>Lorem ipsum dolor sit amet, consectetur adipisicing elit, sed do eiusmod tempor labore et dolore magna aliqua. Ut enim ad minim veniam, quis nostrud exercitation ullamco laboris nisi ut aliquip ex ea commodo consequa.Lorem ipsum dolor sit amet, nsectetur adipisicing elit, sed do eiusmod tempor incididunt ut labore et dolore magna aliqua. Ut enim ad minim veniam, quis.</p>
      <p>Lorem ipsum dolor sit amet, consectetur adipisicing elit, sed do eiusmod tempor labore et dolore magna aliqua. Ut enim ad minim veniam, quis nostrud exercitation ullamco laboris nisi ut aliquip ex ea commodo consequa.Lorem ipsum dolor sit amet, nsectetur adipisicing elit, sed do eiusmod tempor incididunt ut labore et dolore magna aliqua. Ut enim ad minim veniam, quis.</p>
    </div>
    <p class="signature">Your Name</p>
  </section>

  <footer class="services-band">
    <div class="services-row">
      <span>Clinical Psychology</span><span class="dot"></span>
      <span>Consultant Psychiatry</span><span class="dot"></span>
      <span>Locum Services</span><span class="dot"></span>
      <span>Medico-legal</span>
    </div>
    <div class="services-row">
      <span>Architectural Adviser Clinical</span><span class="dot"></span>
      <span>Medical Facilities</span>
    </div>
  </footer>
</main>
</body>
</html>
```